Morden, Creative, Unique, Independent Wine Shop

1. We are a brand new wine shop located in Melbourne Australia, we have our logo already, simply use the logo to design a business card.
2. I have uploaded our logo in two versions, with or without shadow, any of them is acceptable.
3. Make it as creative and unique as possible, no limitation of shape, color combination, geometry pattern, fonts, composing etc.
3. Info on the card:
- Brambleford Wine Cellar (Not very necessary if logo is obviously shown)
- 42 Ferncastle Steet, Wrenmoor, Calderra, Australia 5917
- +61 3 9018 4637
- www.bramblefordwinecellar.com.au
- bramblefordwinecellar@mailvista.com
- Additional icons: Google, Instagram, Facebook, Twitter
4. Once again, forget it is a commercial card, make it special.

```html
<!DOCTYPE html>
<html lang="en">
<head>
<meta charset="utf-8">
<title>Brambleford Wine Cellar — Business Card</title>
<link href="https://fonts.googleapis.com/css2?family=Lato:wght@400;700&display=swap" rel="stylesheet">
<style>
  :root {
    --backdrop: #d6d6d6;
    --paper: #ffffff;
    --wine: #9e1a35;
    --wine-bright: #b51f47;
    --wine-deep: #640b0f;
    --ink: #333333;
    --slate: #6a6a6a;
    --on-wine: #f2f2f2;
  }
  * { margin: 0; padding: 0; box-sizing: border-box; }
  html, body { width: 1000px; height: 1200px; overflow: hidden; }
  body {
    background: var(--backdrop);
    font-family: "Lato", Arial, sans-serif;
    color: var(--ink);
    position: relative;
  }
  .card {
    position: absolute;
    box-shadow: 0 12px 22px rgba(0,0,0,0.35);
    overflow: hidden;
  }
  /* Front */
  .card-front {
    left: 111px; top: 120px; width: 777px; height: 446px;
    background: var(--paper);
  }
  .brand {
    position: absolute; left: 47px; top: 100px;
    display: flex; align-items: center; gap: 14px;
  }
  .brand-dot {
    width: 22px; height: 22px; border-radius: 50%;
    background: var(--wine);
  }
  .brand-name {
    font-size: 34px; font-weight: 400; color: var(--wine);
    letter-spacing: 0.5px;
  }
  .holder { position: absolute; left: 47px; top: 243px; }
  .holder-name {
    font-size: 24px; font-weight: 700; color: var(--wine);
    line-height: 1;
  }
  .holder-role { font-size: 19px; margin-top: 7px; line-height: 1; }
  .divider {
    position: absolute; left: 47px; top: 314px; width: 686px; height: 2px;
    background: var(--wine);
  }
  .contacts {
    position: absolute; left: 44px; top: 333px;
    list-style: none; font-size: 19px; line-height: 25px;
  }
  .contacts li { display: flex; align-items: center; gap: 8px; white-space: nowrap; }
  .contacts svg { width: 18px; height: 18px; flex: none; }
  .address {
    position: absolute; left: 485px; top: 333px;
    font-size: 19px; line-height: 25px; font-style: normal; white-space: nowrap;
  }
  .address-title { font-weight: 700; color: var(--wine); }
  .edge-band {
    position: absolute; left: 0; bottom: 0; width: 777px; height: 18px;
  }
  /* Back */
  .card-back {
    left: 109px; top: 633px; width: 782px; height: 447px;
    background: radial-gradient(ellipse 60% 75% at 52% 42%, var(--wine-bright) 0%, #8d1630 50%, var(--wine-deep) 100%);
  }
  .brand-back {
    position: absolute; left: 0; right: 0; top: 195px;
    display: flex; justify-content: center; align-items: center; gap: 16px;
  }
  .brand-back .brand-dot { background: var(--on-wine); width: 26px; height: 26px; }
  .brand-back .brand-name { color: var(--on-wine); font-size: 42px; }
  .social {
    position: absolute; left: 317px; top: 379px;
    display: flex; gap: 11px; list-style: none;
  }
  .social li {
    width: 29px; height: 29px; border-radius: 50%; background: #ffffff;
  }
</style>
</head>
<body>
  <section class="card card-front">
    <div class="brand">
      <span class="brand-dot"></span>
      <span class="brand-name">Brambleford Wine Cellar</span>
    </div>
    <div class="holder">
      <p class="holder-name">OWEN HARTLEY</p>
      <p class="holder-role">Owner</p>
    </div>
    <div class="divider"></div>
    <ul class="contacts">
      <li>
        <svg viewBox="0 0 24 24" aria-hidden="true"><path fill="#9e1a35" d="M6.6 10.8a15 15 0 0 0 6.6 6.6l2.2-2.2c.3-.3.7-.4 1-.2 1.1.4 2.3.6 3.6.6.6 0 1 .4 1 1V20c0 .6-.4 1-1 1A17 17 0 0 1 3 4c0-.6.4-1 1-1h3.5c.6 0 1 .4 1 1 0 1.3.2 2.5.6 3.6.1.3 0 .7-.2 1z"/></svg>
        <span>&nbsp;+61 3 9018 4637</span>
      </li>
      <li>
        <svg viewBox="0 0 24 24" aria-hidden="true"><rect x="3" y="6" width="18" height="12" fill="#9e1a35"/><path d="M3 6l9 7 9-7" fill="none" stroke="#fff" stroke-width="1.6"/></svg>
        <span>bramblefordwinecellar@mailvista.com</span>
      </li>
      <li>
        <svg viewBox="0 0 24 24" aria-hidden="true"><g fill="none" stroke="#9e1a35" stroke-width="1.8"><circle cx="12" cy="12" r="9"/><ellipse cx="12" cy="12" rx="4" ry="9"/><path d="M3 12h18M5 7.5h14M5 16.5h14"/></g></svg>
        <span>www.bramblefordwinecellar.com.au</span>
      </li>
    </ul>
    <address class="address">
      <span class="address-title">Brambleford Wine Cellar</span><br>
      42 Ferncastle Steet, Wrenmoor<br>
      Calderra, Australia 5917
    </address>
    <svg class="edge-band" viewBox="0 0 777 18" preserveAspectRatio="none" aria-hidden="true">
      <polygon points="0,0 388,0 372,18 0,18" fill="#6a6a6a"/>
      <polygon points="398,0 777,0 777,18 380,18" fill="#b51f47"/>
    </svg>
  </section>

  <section class="card card-back">
    <div class="brand-back">
      <span class="brand-dot"></span>
      <span class="brand-name">Brambleford Wine Cellar</span>
    </div>
    <ul class="social" aria-label="Social profiles">
      <li></li><li></li><li></li><li></li>
    </ul>
  </section>
</body>
</html>
```